Business Card design for a skin clinic

i would like a business card design for our skin clinic.
our logo colors are Blue and Grey and Bule /white.
we are searching for a minimalistic design yet very elegant,dynamic and professional which can reflect a professional medical skin care clinic( not a beauty salon).
THE DESGIN IS NOT FOR A PERSON IT WILL BE USED IN THE CLINIC FOR CLIENTS SO THERE SHOULD BE NO NAME OF A PERSON ONLY THE CLINIC NAME AND THE CONTACT INFO

Target Market(s)
young and old womens
Industry/Entity Type
Business
Contact Information for Business Card
we have 2 address and both should be on the card.
address A: Lindenhoflaan 214B, 3041KP Rotterdam, Tel 010 483 21 95
address B: Zonnewijzerstraat 238, 1062RT Amsterdam Tel 020 571 3829
website www.huidpuntzorg.nu, email info@huidpuntzorg.nu
Look and feel
Each slider illustrates characteristics of the customer's brand and the style your logo design should communicate.

```html
<!DOCTYPE html>
<html lang="nl">
<head>
<meta charset="utf-8">
<title>Huidpuntzorg – visitekaartje</title>
<link rel="stylesheet" href="https://fonts.googleapis.com/css2?family=Raleway:wght@400&family=Lato:wght@400&family=Arimo:wght@400&display=swap">
<style>
  :root {
    --page: #ffffff;
    --navy-deep: #1f2a44;
    --navy: #2b3d66;
    --navy-light: #3d5078;
    --rim: #262d3f;
    --silver-light: #ffffff;
    --silver: #cfcfd1;
    --ink-light: #ffffff;
    --brand: #e6e9ef;
  }
  * { box-sizing: border-box; margin: 0; padding: 0; }
  html, body { width: 1200px; height: 1000px; overflow: hidden; background: var(--page); }
  .canvas { position: relative; width: 1200px; height: 1000px; }
  .card {
    position: absolute; left: 187px; width: 826px; height: 478px; overflow: hidden;
  }
  .card--front { top: 12px; background: linear-gradient(100deg, var(--silver-light) 55%, var(--silver) 100%); }
  .card--back { top: 508px; height: 480px; background: var(--page); }
  .card__field { position: absolute; inset: 0; width: 100%; height: 100%; }
  .brand {
    position: absolute; left: 0; width: 100%; text-align: center; color: var(--brand);
  }
  .brand__name {
    font-family: "Raleway", sans-serif; font-weight: 400; font-size: 40px;
    letter-spacing: 4px; line-height: 1;
  }
  .brand__tagline {
    margin-top: 14px; font-family: "Lato", sans-serif; font-size: 13px;
    letter-spacing: 0.8px; color: var(--ink-light);
  }
  .card--front .brand { top: 150px; }
  .card--back .brand { top: 230px; }
  .contact {
    position: absolute; display: flex; align-items: center; color: var(--ink-light);
    font-family: "Arimo", sans-serif; font-size: 20px; white-space: nowrap;
  }
  .contact svg { position: absolute; left: 0; }
  .contact__text { margin-left: 37px; }
  .contact--phone .contact__text { margin-left: 36px; }
</style>
</head>
<body>
<div class="canvas">

  <section class="card card--front">
    <svg class="card__field" viewBox="0 0 826 478" role="img" aria-label="Donkerblauw facetpatroon van veelhoeken">
      <defs>
        <linearGradient id="navyFront" x1="0" y1="0" x2="1" y2="1">
          <stop offset="0" stop-color="#262c3d"/>
          <stop offset="0.35" stop-color="#2b3d66"/>
          <stop offset="0.6" stop-color="#3a4b70"/>
          <stop offset="1" stop-color="#232b42"/>
        </linearGradient>
      </defs>
      <path d="M0 0 H413 C650 20 832 130 826 250 C820 350 720 430 620 478 H0 Z" fill="url(#navyFront)" stroke="var(--rim)" stroke-width="8"/>
    </svg>

    <div class="brand">
      <div class="brand__name">HUIDPUNTZORG</div>
      <div class="brand__tagline">next Generation Skin Care</div>
    </div>

    <div class="contact contact--address" style="left:14px; top:251px; height:28px;">
      <svg width="34" height="32" viewBox="0 0 34 32"><path d="M17 3a8 8 0 0 0-8 8c0 6 8 14 8 14s8-8 8-14a8 8 0 0 0-8-8z" fill="none" stroke="#fff" stroke-width="1.4"/><circle cx="17" cy="11" r="3" fill="none" stroke="#fff" stroke-width="1.4"/><ellipse cx="17" cy="26" rx="15" ry="4" fill="none" stroke="#fff" stroke-width="1.2"/></svg>
      <span class="contact__text" style="margin-left:53px;">Lindenhoflaan 214B, 3041KP Rotterdam</span>
    </div>
    <div class="contact contact--address" style="left:14px; top:307px; height:28px;">
      <svg width="34" height="32" viewBox="0 0 34 32"><path d="M17 3a8 8 0 0 0-8 8c0 6 8 14 8 14s8-8 8-14a8 8 0 0 0-8-8z" fill="none" stroke="#fff" stroke-width="1.4"/><circle cx="17" cy="11" r="3" fill="none" stroke="#fff" stroke-width="1.4"/><ellipse cx="17" cy="26" rx="15" ry="4" fill="none" stroke="#fff" stroke-width="1.2"/></svg>
      <span class="contact__text" style="margin-left:53px;">Zonnewijzerstraat 238, 1062RT Amsterdam</span>
    </div>
    <div class="contact contact--email" style="left:10px; top:362px; height:28px;">
      <svg width="38" height="28" viewBox="0 0 38 28"><rect x="1" y="2" width="36" height="24" fill="#fff"/><path d="M1 2 L19 16 L37 2 M1 26 L14 12 M37 26 L24 12" fill="none" stroke="var(--navy)" stroke-width="1.8"/></svg>
      <span class="contact__text" style="margin-left:59px;">info@huidpuntzorg.nu</span>
    </div>
    <div class="contact contact--web" style="left:12px; top:410px; height:36px;">
      <svg width="36" height="36" viewBox="0 0 36 36" fill="none" stroke="#fff" stroke-width="2"><circle cx="18" cy="18" r="16"/><ellipse cx="18" cy="18" rx="7" ry="16"/><path d="M2 18h32M18 2v32M5 10h26M5 26h26"/></svg>
      <span class="contact__text" style="margin-left:57px;">www.huidpuntzorg.nu</span>
    </div>

    <div class="contact contact--phone" style="left:543px; top:250px; height:36px;">
      <svg width="34" height="36" viewBox="0 0 34 36" fill="none" stroke="#fff" stroke-width="1.4"><rect x="10" y="2" width="14" height="30" rx="2"/><path d="M10 7h14M10 27h14"/><path d="M6 8c-2 3-2 7 0 10M3 6c-3 4-3 10 0 14M28 8c2 3 2 7 0 10M31 6c3 4 3 10 0 14"/></svg>
      <span class="contact__text">010 483 21 95</span>
    </div>
    <div class="contact contact--phone" style="left:543px; top:306px; height:36px;">
      <svg width="34" height="36" viewBox="0 0 34 36" fill="none" stroke="#fff" stroke-width="1.4"><rect x="10" y="2" width="14" height="30" rx="2"/><path d="M10 7h14M10 27h14"/><path d="M6 8c-2 3-2 7 0 10M3 6c-3 4-3 10 0 14M28 8c2 3 2 7 0 10M31 6c3 4 3 10 0 14"/></svg>
      <span class="contact__text">020 571 3829</span>
    </div>
  </section>

  <section class="card card--back">
    <svg class="card__field" viewBox="0 0 826 480" role="img" aria-label="Donkerblauw facetpatroon van veelhoeken">
      <defs>
        <linearGradient id="navyBack" x1="0" y1="0" x2="1" y2="1">
          <stop offset="0" stop-color="#262c3d"/>
          <stop offset="0.35" stop-color="#2b3d66"/>
          <stop offset="0.6" stop-color="#3a4b70"/>
          <stop offset="1" stop-color="#232b42"/>
        </linearGradient>
      </defs>
      <path d="M0 0 H333 C600 20 800 150 832 230 V486 H420 C250 440 80 300 -4 178 Z" fill="url(#navyBack)" stroke="var(--rim)" stroke-width="8"/>
    </svg>

    <div class="brand">
      <div class="brand__name">HUIDPUNTZORG</div>
      <div class="brand__tagline">next Generation Skin Care</div>
    </div>
  </section>

</div>
</body>
</html>
```